International Petrochemical business needs a web design for Tessaro Desk system

We need a web design for a "Tessaro Desk" system for an international petrochemical company. The web site is used internally within the company. It is hosted by an internal department which provides government permit request service for other departments.

We would like to see designs of two pages using color light blue. (home page, internal page as attached).
Home Page:
1. Header has a background image and small animation. Header on home page can be taller than the header of the internal page.
2. Layout as attached.

Internal Page:
1. Header can use the same background image as the home page and can be shorter to utilize the page for content.
2. The blue icon behind every captions represent an icon. When user move mouse over this icon, it displays the caption in Thai language as a tooltip. This icon needs to be redesign.

The final design should communicate the followings:
- Excellent service provided system in terms of time and accurary
- Rapid growth of business via building petrochemical refinery plant

For Internal Page, the blue circle behind every captions represent an icon. When mouse over this icon, a tool tip showing the caption in Thai language is shown. Please also design this icon..

There are more feedbacks from customer as followed:

1. Banner should consists of 
    1.1 "Approved" stamp on paper
    1.2 An image of Garuda. It is used on every government documents in Thailand
    1.3 Image of petrochemical plant
2. Each menu item (Home, Permit, Search, etc) should have different colors. Drop down menu will use the same color as its parent menu item.
3. Overall tone of the web page should be light blue with background of the body the web page in white
4. "New Request" button should use green color with icon on it
5. Table header of each box in the body of the page should use dark blue background with text in white

Please kindly submit your revisions.
Thank you.

Reason: We get some late feedbacks from customers which was just updated to all designers.

• 1. Design for 1024x768 screen resolution
2. Use light blue theme
3. Background of header where the company logo is must have white background

```html
<!DOCTYPE html>
<html lang="en">
<head>
<meta charset="utf-8">
<title>Tessaro Desk – Home</title>
<link rel="stylesheet" href="https://fonts.googleapis.com/css2?family=Open+Sans:wght@400;600;700&family=Arimo:wght@400&display=swap">
<style>
:root{
  --ink:#2b2b2b;
  --text:#444;
  --accent:#1aa6e4;
  --link:#0b4fa8;
  --mark:#8a8a8a;
  --band-top:#0d5a9c;
  --band-mid:#1e9be0;
  --band-bot:#2bb2ec;
  --panel:#f4f4f4;
  --panel-low:#e6e6e6;
  --th:#333333;
  --row-line:#dcdcdc;
  --green-top:#9ed84a;
  --green-bot:#6db521;
}
*{box-sizing:border-box;margin:0;padding:0}
html,body{width:1174px;height:1200px;overflow:hidden}
body{position:relative;font-family:"Open Sans",Arial,sans-serif;color:var(--text);background:var(--panel)}
.abs{position:absolute}
a{text-decoration:underline}

/* header */
.top-rule{left:0;top:0;width:1174px;height:4px;background:#3a3a3a}
.masthead{left:0;top:4px;width:1174px;height:122px;background:linear-gradient(#f2f2f2,#e4e4e4)}
.brand{left:122px;top:30px;height:36px;display:flex;align-items:center;gap:10px}
.brand-square{width:26px;height:26px;background:var(--mark)}
.brand-name{font-weight:600;font-size:18px;line-height:22px;color:#333;white-space:nowrap}
.brand-rule{left:317px;top:50px;width:1px;height:30px;background:#999}
.product{left:331px;top:54px;font-size:15px;font-weight:600;color:#333}
.nav{left:506px;top:43px;display:flex;font-family:Arimo,Arial,sans-serif;font-size:14px;color:#333}
.nav a{color:#333;text-decoration:none;height:30px;line-height:30px;margin-right:24px}
.nav a.current{padding:0 13px;border:1px solid #b8b8b8;border-radius:9px;background:linear-gradient(#fafafa,#dcdcdc);box-shadow:0 1px 2px rgba(0,0,0,.15)}
.search{left:864px;top:38px;width:191px;height:42px;border:1px solid #bdbdbd;border-radius:7px;background:linear-gradient(#fafafa,#dedede);box-shadow:0 2px 3px rgba(0,0,0,.12)}
.search-field{position:absolute;left:9px;top:10px;width:130px;height:21px;border-radius:11px;background:#e6e6e6;box-shadow:inset 0 1px 3px rgba(0,0,0,.3)}
.search-sep{position:absolute;left:150px;top:0;width:1px;height:40px;background:#c4c4c4}
.search svg{position:absolute;left:159px;top:9px}

/* band + banner */
.band{left:0;top:126px;width:1174px;height:258px;background:linear-gradient(var(--band-top) 0%,var(--band-mid) 55%,var(--band-bot) 100%);border-bottom:2px solid #1a6fa8}
.hero{left:118px;top:96px;width:938px;height:226px;background:linear-gradient(180deg,#4e4f86 0%,#8d76a6 35%,#3a4662 70%,#1b2431 100%)}
.hero-caption{left:506px;top:144px;width:550px;height:108px;background:rgba(30,30,35,.72);padding:10px 20px;color:#fff;font-family:Arimo,Arial,sans-serif}
.hero-caption h1{font-weight:400;font-size:30px;line-height:36px}
.hero-caption p{font-size:13px;line-height:17px;margin-top:8px}
.hero-caption a{color:#5ec8f4;font-style:italic}
.slider-tab{left:514px;top:348px;width:158px;height:36px;background:linear-gradient(#555,#333);border-radius:14px 14px 0 0}
.slider-dots{left:550px;top:360px;display:flex;gap:13px}
.slider-dots span{width:13px;height:13px;border-radius:50%;background:#1d1d1d;box-shadow:inset 0 1px 2px #000}
.slider-dots span.on{background:#fff}

/* panels */
.lower{left:0;top:824px;width:1174px;height:332px;background:var(--panel-low);border-top:1px solid #c8c8c8}
.box-title{font-size:25px;font-weight:600;color:var(--ink);line-height:30px}
.box-title em{font-style:normal;color:var(--accent)}
table{border-collapse:collapse;font-size:13px}
th{background:var(--th);color:#fff;font-weight:600;text-align:left;height:31px;padding:0 7px;border-left:1px solid #666}
th:first-child{border-left:none}
td{height:30px;padding:0 7px;border-bottom:1px solid var(--row-line);color:#444}
td a{color:var(--link)}
.num{text-align:center}
.box-base{height:1px;background:var(--row-line)}

.pager{display:flex;gap:3px;align-items:center}
.pager .step{width:26px;height:26px;border-radius:7px;background:linear-gradient(#5a7aa0,#2d4767)}
.pager .step svg{display:block;margin:7px auto}
.pager .page{width:21px;height:23px;line-height:21px;text-align:center;font-size:13px;color:#555;border:1px solid #bdbdbd;background:linear-gradient(#fff,#e6e6e6)}

.flag{display:inline-block;width:11px;height:11px;border-radius:50%;vertical-align:-1px;margin-left:4px}
.flag.red{background:#e03020}
.flag.amber{background:#f3c21a}

.new-request{left:614px;top:854px;width:437px;height:51px;border:1px solid #5aa01a;border-radius:4px;background:linear-gradient(var(--green-top),var(--green-bot));color:#234b0a;font-size:16px;text-align:center;line-height:49px}

.footer{left:0;top:1156px;width:1174px;height:44px;background:linear-gradient(#5a5a5a,#3b3b3b);color:#fff;font-family:Arimo,Arial,sans-serif;font-size:12px;line-height:44px;text-align:center;word-spacing:2px}
.footer span{margin:0 10px}
</style>
</head>
<body>

<div class="abs top-rule"></div>
<header class="abs masthead"></header>
<div class="abs brand"><div class="brand-square"></div><div class="brand-name">Kestrel Group</div></div>
<div class="abs brand-rule"></div>
<div class="abs product">Tessaro Desk</div>
<nav class="abs nav"><a class="current">Home</a><a>Permits</a><a>Reports</a><a>Admin</a><a>Help</a></nav>
<div class="abs search">
  <div class="search-field"></div>
  <div class="search-sep"></div>
  <svg width="24" height="24" viewBox="0 0 24 24"><circle cx="10" cy="10" r="7" fill="none" stroke="#333" stroke-width="3"/><line x1="15" y1="15" x2="22" y2="22" stroke="#333" stroke-width="3.5" stroke-linecap="round"/></svg>
</div>

<div class="abs band"></div>
<div class="abs hero" role="img" aria-label="Petrochemical refinery plant lit at dusk under a purple sky"></div>
<div class="abs hero-caption">
  <h1>Buy with confidence.</h1>
  <p>We have industry leading processes and procedures to ensure nothing but the most reliable product. <a>Find out more about our commitment to our customers.</a></p>
</div>
<div class="abs slider-tab"></div>
<div class="abs slider-dots"><span class="on"></span><span></span><span></span><span></span></div>

<!-- New Requests -->
<h2 class="abs box-title" style="left:121px;top:397px"><em>New</em> Requests</h2>
<table class="abs" style="left:121px;top:431px;width:438px">
  <tr><th style="width:106px">Request No.</th><th style="width:138px">Requested Date</th><th>Branch</th></tr>
  <tr><td><a>56-0003</a></td><td>20/4/2013</td><td>GC1</td></tr>
  <tr><td><a>56-0004</a></td><td>20/4/2013</td><td>GC2</td></tr>
</table>
<div class="abs box-base" style="left:121px;top:582px;width:438px"></div>
<div class="abs pager" style="left:265px;top:588px"><div class="step"><svg width="8" height="12"><path d="M6 1L2 6l4 5" fill="none" stroke="#fff" stroke-width="2"/></svg></div><div class="page">1</div><div class="page">2</div><div class="page">3</div><div class="page">4</div><div class="step"><svg width="8" height="12"><path d="M2 1l4 5-4 5" fill="none" stroke="#fff" stroke-width="2"/></svg></div></div>
<div class="abs box-base" style="left:121px;top:619px;width:438px"></div>

<!-- My Working Requests -->
<h2 class="abs box-title" style="left:613px;top:397px"><em>My Working</em> Requests</h2>
<table class="abs" style="left:613px;top:431px;width:438px">
  <tr><th style="width:106px">Request No.</th><th style="width:120px">Requested Date</th><th>Status</th></tr>
  <tr><td><a>55-0200</a></td><td>20/4/2013</td><td>Waiting for process</td></tr>
  <tr><td><a>55-0210</a></td><td>20/4/2013</td><td>In progress</td></tr>
  <tr><td><a>55-0300</a></td><td>20/4/2013</td><td>Incomplete document</td></tr>
  <tr><td><a>55-0301</a></td><td>20/4/2013</td><td>Cancel requested</td></tr>
</table>
<div class="abs pager" style="left:757px;top:588px"><div class="step"><svg width="8" height="12"><path d="M6 1L2 6l4 5" fill="none" stroke="#fff" stroke-width="2"/></svg></div><div class="page">1</div><div class="page">2</div><div class="page">3</div><div class="page">4</div><div class="step"><svg width="8" height="12"><path d="M2 1l4 5-4 5" fill="none" stroke="#fff" stroke-width="2"/></svg></div></div>
<div class="abs box-base" style="left:613px;top:619px;width:438px"></div>

<!-- Expiring Permits -->
<h2 class="abs box-title" style="left:121px;top:638px"><em>Expiring</em> Permits</h2>
<table class="abs" style="left:121px;top:672px;width:930px">
  <tr><th style="width:114px">Permit No</th><th style="width:119px">Expire Date</th><th style="width:246px">Permit Name</th><th style="width:116px">Branch</th><th style="width:153px">Required Time (Day)</th><th>Required Time (Day)</th></tr>
  <tr><td><a>AB56001</a></td><td>25/3/2013</td><td>Permit Name ###10</td><td>GC1</td><td class="num">30<span class="flag red"></span></td><td class="num">-40</td></tr>
  <tr><td><a>BIO5502</a></td><td>24/3/2013</td><td>Permit Name ###20</td><td>GC2</td><td class="num">60<span class="flag amber"></span></td><td class="num">15</td></tr>
</table>
<div class="abs pager" style="left:500px;top:768px"><div class="step"><svg width="8" height="12"><path d="M6 1L2 6l4 5" fill="none" stroke="#fff" stroke-width="2"/></svg></div><div class="page">1</div><div class="page">2</div><div class="page">3</div><div class="page">4</div><div class="step"><svg width="8" height="12"><path d="M2 1l4 5-4 5" fill="none" stroke="#fff" stroke-width="2"/></svg></div></div>
<div class="abs box-base" style="left:121px;top:799px;width:906px"></div>

<!-- lower section -->
<div class="abs lower"></div>

<h2 class="abs box-title" style="left:122px;top:847px"><em>My In Progress</em> Requests</h2>
<table class="abs" style="left:124px;top:886px;width:436px">
  <tr><th style="width:106px">Request No.</th><th style="width:143px">Requested Date</th><th>Status</th></tr>
  <tr><td><a>56-0003</a></td><td>20/4/2013</td><td>ระหว่างดำเนินการ</td></tr>
  <tr><td><a>56-0004</a></td><td>20/4/2013</td><td>รอดำเนินการ</td></tr>
</table>
<div class="abs box-base" style="left:124px;top:1073px;width:436px"></div>
<div class="abs pager" style="left:267px;top:1079px"><div class="step"><svg width="8" height="12"><path d="M6 1L2 6l4 5" fill="none" stroke="#fff" stroke-width="2"/></svg></div><div class="page">1</div><div class="page">2</div><div class="page">3</div><div class="page">4</div><div class="step"><svg width="8" height="12"><path d="M2 1l4 5-4 5" fill="none" stroke="#fff" stroke-width="2"/></svg></div></div>

<div class="abs new-request">New Request</div>

<h2 class="abs box-title" style="left:613px;top:913px"><em>Recent Completed</em> Requests</h2>
<table class="abs" style="left:615px;top:951px;width:436px">
  <tr><th style="width:135px">Request No.</th><th>Completed Date</th></tr>
  <tr><td><a>55-0100</a></td><td>20/4/2013</td></tr>
  <tr><td><a>55-0088</a></td><td>20/4/2013</td></tr>
  <tr><td><a>55-0002</a></td><td>20/4/2013</td></tr>
</table>
<div class="abs pager" style="left:757px;top:1078px"><div class="step"><svg width="8" height="12"><path d="M6 1L2 6l4 5" fill="none" stroke="#fff" stroke-width="2"/></svg></div><div class="page">1</div><div class="page">2</div><div class="page">3</div><div class="page">4</div><div class="step"><svg width="8" height="12"><path d="M2 1l4 5-4 5" fill="none" stroke="#fff" stroke-width="2"/></svg></div></div>

<footer class="abs footer">Copyright 2013 KESTREL GROUP <span>Home</span>|<span>Permits</span>|<span>Repots</span>|<span>Search</span>|<span>Admin</span>|<span>Help</span></footer>

</body>
</html>
```